New Coffee Shop business card

We are opening our new coffee shop and are needing business cards to take with us on February 6th to Atlanta, Ga to a show.

We will be offering the following menu type items:

coffee
teas
espresso
frappes
smoothies

sandwiches
soups
salads
pastries
ice cream

Our shop is in a rural country-side area and we would like to convey that feel in our shop. In addition to the cafe we will also be selling gifts and furniture and other home decor. Much of this merchandise will be rescued, refurbished or repurposed which is also a core value of what we are all about.

We have a company logo we would like incorporated into the design.

We will also provide files that have the elements of the logo which may also be useful in the design of the card.

Since we are not open yet we need one slightly altered version of the card as well as the final product which states "Opening in the summer 2015"

Target Market(s)

moderate to slightly upscale and folksy.

Industry/Entity Type

Coffee Shop

Contact Information for Business Card

Fern Hollow Coffee
name
address
phone number
email

Card

Font styles to use
Sans Serif

Requirements
Must have
• Must include Logo
• Must include information on menu.
• Must include information on our merchandise sales as described inthe project description.
• Color scheme to complement the logo
Nice to have
• The following descriptions
• "We are also selling gifts, furniture, and other home decoration."
• "We rescue, refurbish, and repurpose old furniture so it can live again."

```html
<!DOCTYPE html>
<html lang="en">
<head>
<meta charset="utf-8">
<title>Fern Hollow Coffee – Business Cards</title>
<link rel="stylesheet" href="https://fonts.googleapis.com/css2?family=Marcellus+SC&family=Questrial&display=swap">
<style>
  :root {
    --page-bg: #e4e2df;
    --front-bg: #2b2526;
    --front-text: #ffffff;
    --back-bg: #ffffff;
    --back-text: #3a3533;
    --photo-warm: #e9c79a;
    --photo-cream: #f4ece2;
    --photo-steel: #bdb7b1;
  }
  * { margin: 0; padding: 0; box-sizing: border-box; }
  html, body {
    width: 1200px;
    height: 1000px;
    overflow: hidden;
    background: var(--page-bg);
  }
  .canvas {
    position: relative;
    width: 1200px;
    height: 1000px;
  }
  .card {
    position: absolute;
    left: 280px;
    width: 640px;
    height: 366px;
    overflow: hidden;
    box-shadow: 0 6px 18px rgba(0,0,0,0.18);
  }

  /* Front card */
  .card-front {
    top: 70px;
    background: var(--front-bg);
    color: var(--front-text);
  }
  .card-front .brand {
    position: absolute;
    top: 36px;
    left: 0;
    width: 100%;
    text-align: center;
    font-family: "Questrial", sans-serif;
    font-size: 15px;
    letter-spacing: 0.5px;
    color: var(--front-text);
  }
  .contact {
    position: absolute;
    top: 150px;
    right: 60px;
    list-style: none;
    text-align: center;
    font-family: "Marcellus SC", sans-serif;
    font-size: 21px;
    line-height: 34px;
    letter-spacing: 1px;
  }

  /* Back card */
  .card-back {
    top: 530px;
    background: var(--back-bg);
    color: var(--back-text);
    font-family: "Questrial", sans-serif;
  }
  .coffee-photo {
    position: absolute;
    inset: 0;
    background:
      radial-gradient(ellipse 45% 55% at 45% 82%, var(--photo-steel) 0%, rgba(189,183,177,0) 70%),
      radial-gradient(ellipse 70% 60% at 20% 90%, var(--photo-warm) 0%, rgba(233,199,154,0) 75%),
      linear-gradient(160deg, #ffffff 30%, var(--photo-cream) 75%, #efe4d6 100%);
  }
  .back-content {
    position: absolute;
    inset: 0;
    text-align: center;
  }
  .merch {
    margin-top: 30px;
    font-size: 16px;
    line-height: 22px;
  }
  .menu-title {
    margin-top: 12px;
    font-size: 16px;
  }
  .menu {
    display: flex;
    justify-content: center;
    gap: 80px;
    margin-top: 2px;
    list-style: none;
  }
  .menu ul {
    list-style: none;
    font-size: 16px;
    line-height: 19px;
  }
  .opening {
    margin-top: 14px;
    font-size: 17px;
  }
  .card-back .brand {
    margin-top: 12px;
    font-size: 13px;
    color: var(--back-text);
  }
</style>
</head>
<body>
<main class="canvas">

  <section class="card card-front">
    <div class="brand">Fern Hollow Coffee</div>
    <ul class="contact">
      <li>Your Name Your Name</li>
      <li>Address, Country, State, Zip 000000</li>
      <li>000 0000 0000</li>
      <li>your_email@company.com</li>
    </ul>
  </section>

  <section class="card card-back">
    <div class="coffee-photo" role="img" aria-label="Soft photo of an espresso portafilter filled with ground coffee"></div>
    <div class="back-content">
      <p class="merch">We are also selling gifts, furniture, and other home decoration.<br>
        We rescue, refurbish, and repurpose old furniture so it can live again.</p>
      <p class="menu-title">Menu:</p>
      <div class="menu">
        <ul>
          <li>Coffee</li>
          <li>Teas</li>
          <li>Espresso</li>
          <li>Frappes</li>
          <li>Smoothies</li>
        </ul>
        <ul>
          <li>Sandwiches</li>
          <li>Soups</li>
          <li>Salads</li>
          <li>Pastries</li>
          <li>Ice cream</li>
        </ul>
      </div>
      <p class="opening">Opening in the summer 2015.</p>
      <div class="brand">Fern Hollow Coffee</div>
    </div>
  </section>

</main>
</body>
</html>
```